Business card and stationery concept for weight management and nutrition practice
trueLeaf Guidance
Dear Designers,
I have uploaded my logo files and am looking forward to everyone's designs.
I would like to see designs that do not feature my logo quite so prominently - that is, the logo does not have to be very large.
Also, instead of bold abstract curves and shapes I'd like to see accents that are more feminine.
Thanks everyone!
I like the bold concepts you have uploaded. I would also like to see more simple ideas, using the light blue and dark grey used in the logo rather than black.
I would also like to see a few concepts that are a bit more feminine. Not overtly so but subtle.
Thank you!
I am unable to upload my logo at this time -- I will do this on Saturday evening when I get back in town.

```html
<!DOCTYPE html>
<html lang="en">
<head>
<meta charset="utf-8">
<title>trueLeaf Guidance – Business Card</title>
<link rel="stylesheet" href="https://fonts.googleapis.com/css2?family=Montserrat:wght@400;600&display=swap">
<style>
  :root {
    --backdrop: #e8e6e2;
    --card-white: #ffffff;
    --accent-blue: #5aa9d6;
    --charcoal-dark: #2f3032;
    --charcoal-light: #5b5c5f;
    --ink-grey: #4a4b4e;
    --muted-grey: #8d8e91;
    --text-light: #f2f2f2;
  }
  * { margin: 0; padding: 0; box-sizing: border-box; }
  html, body {
    width: 1200px; height: 629px; overflow: hidden;
    background: var(--backdrop);
    font-family: "Montserrat", sans-serif;
  }
  .canvas {
    position: relative; width: 1200px; height: 629px;
    display: flex; align-items: center; justify-content: center; gap: 60px;
  }
  .card {
    position: relative; width: 500px; height: 286px;
    background: var(--card-white);
    box-shadow: 0 6px 18px rgba(0,0,0,0.12);
    overflow: hidden;
  }
  .brand {
    display: flex; flex-direction: column; align-items: center; gap: 10px;
  }
  .brand-square {
    width: 18px; height: 18px; background: var(--accent-blue);
  }
  .brand-name {
    font-weight: 600; font-size: 26px; letter-spacing: 0.5px;
    color: var(--ink-grey);
  }
  .card-front {
    display: flex; flex-direction: column; align-items: center; justify-content: center; gap: 22px;
  }
  .front-web {
    font-size: 11px; letter-spacing: 1.5px; color: var(--muted-grey);
  }
  .card-back .back-top {
    height: 150px; display: flex; align-items: center; justify-content: center;
  }
  .card-back .brand-name { font-size: 22px; }
  .card-back .brand-square { width: 15px; height: 15px; }
  .back-rule {
    height: 3px; background: var(--accent-blue);
  }
  .back-bottom {
    height: 133px;
    background: linear-gradient(180deg, var(--charcoal-light) 0%, var(--charcoal-dark) 100%);
    display: flex; justify-content: space-between; align-items: flex-end;
    padding: 0 26px 24px 26px;
    color: var(--text-light);
  }
  .person-name { font-size: 12px; font-weight: 600; letter-spacing: 0.4px; }
  .person-title { font-size: 9.5px; margin-top: 4px; color: #c9cacc; letter-spacing: 0.4px; }
  .contact-list { list-style: none; display: flex; flex-direction: column; gap: 7px; }
  .contact-item { display: flex; align-items: center; gap: 8px; font-size: 9.5px; letter-spacing: 0.3px; }
  .contact-icon {
    width: 14px; height: 14px; border-radius: 50%; background: var(--text-light);
    display: flex; align-items: center; justify-content: center; flex-shrink: 0;
  }
  .contact-icon svg { width: 9px; height: 9px; }
</style>
</head>
<body>
<main class="canvas">
  <section class="card card-front">
    <div class="brand">
      <span class="brand-square"></span>
      <span class="brand-name">trueLeaf Guidance</span>
    </div>
    <p class="front-web">www.trueLeafGuidance.com</p>
  </section>

  <section class="card card-back">
    <div class="back-top">
      <div class="brand">
        <span class="brand-square"></span>
        <span class="brand-name">trueLeaf Guidance</span>
      </div>
    </div>
    <div class="back-rule"></div>
    <div class="back-bottom">
      <div class="person">
        <p class="person-name">Nora Whitfield, MS, RD, LDN</p>
        <p class="person-title">Registered Dietitian</p>
      </div>
      <ul class="contact-list">
        <li class="contact-item">
          <span class="contact-icon"><svg viewBox="0 0 10 10"><path d="M5 1a3 3 0 0 1 3 3c0 2-3 5-3 5S2 6 2 4a3 3 0 0 1 3-3z" fill="#3a3b3d"/><circle cx="5" cy="4" r="1" fill="#f2f2f2"/></svg></span>
          240 Willow Creek Road, Suite 5
        </li>
        <li class="contact-item">
          <span class="contact-icon"><svg viewBox="0 0 10 10"><path d="M2.5 1.5l1.5 0 .8 2-1 .8a5 5 0 0 0 2 2l.8-1 2 .8v1.5c0 .5-.5 1-1 1A7 7 0 0 1 1.5 2.5c0-.5.5-1 1-1z" fill="#3a3b3d"/></svg></span>
          (555) 014-2270
        </li>
        <li class="contact-item">
          <span class="contact-icon"><svg viewBox="0 0 10 10"><rect x="1.5" y="2.5" width="7" height="5" fill="#3a3b3d"/><path d="M1.5 2.5l3.5 3 3.5-3" stroke="#f2f2f2" stroke-width="0.8" fill="none"/></svg></span>
          nora@trueleafguidance.com
        </li>
        <li class="contact-item">
          <span class="contact-icon"><svg viewBox="0 0 10 10"><circle cx="5" cy="5" r="3.5" stroke="#3a3b3d" stroke-width="0.9" fill="none"/><ellipse cx="5" cy="5" rx="1.5" ry="3.5" stroke="#3a3b3d" stroke-width="0.7" fill="none"/><line x1="1.5" y1="5" x2="8.5" y2="5" stroke="#3a3b3d" stroke-width="0.7"/></svg></span>
          www.trueleafguidance.com
        </li>
      </ul>
    </div>
  </section>
</main>
</body>
</html>
```